Card front cover, made up of words and statements, similar to the front of a tovarinda bag.

I'm looking to design the front of a card or post card I will use in my business. I want to use a mash up of words and statements and sentences to inspire my audience. The card should be visually nice and use various fonts. My business inspires kids to set goals and dream big. You can use the "moon" shape as seen in my logo, but stick to mostly the words and statements listed on the attached word document or other similar statements you find, the shorter statements tend to look better. I'm interested to see a use of different fonts and sizes. All with a "modern" look and feel.

Target Market(s)

parents of children ages 8-12

Industry/Entity Type

Party space: specifically slumber parties

Font styles to use
Other font styles liked:
• Avenir Next LT pro

Colors
FFC000
F8CF3A
FAE287
FDF2CF
FEFAEE

Requirements
Must have
• The use of the "moon" logo and the words: Sleep Less, Dream More
Nice to have
• I made a long list of inspirational quotes to use, they don't all need to be used but that is the idea I'm looking for. After looking at designs the long sentences do NOT work as well. Please either shorten them or find other similar statements.
Should not have
• color, please use the yellow as shown in my moon logo, black and white

```html
<!DOCTYPE html>
<html lang="en">
<head>
<meta charset="utf-8">
<title>Dream More – Card Front</title>
<link rel="stylesheet" href="https://fonts.googleapis.com/css2?family=Arimo:wght@400;700&family=Lato:wght@400&family=Libre+Bodoni:wght@400;700&display=swap">
<style>
  :root {
    --ink: #333333;
    --sun: #FDD02A;
    --sun-deep: #FFC61E;
    --sun-light: #FFF45C;
    --paper: #FFFFFF;
  }
  html, body {
    margin: 0;
    padding: 0;
    width: 1200px;
    height: 938px;
    overflow: hidden;
    background: var(--paper);
  }
  .canvas {
    position: relative;
    width: 1200px;
    height: 938px;
    background: var(--paper);
  }
  .card {
    position: absolute;
    left: 83px;
    top: 71px;
    width: 1038px;
    height: 778px;
    background: linear-gradient(150deg, var(--sun-deep) 0%, var(--sun) 45%, var(--sun-light) 100%);
    overflow: hidden;
  }
  .card > * { position: absolute; margin: 0; color: var(--ink); }
  .serif { font-family: "Libre Bodoni", "Bodoni Moda", serif; }
  .sans { font-family: "Arimo", Arial, sans-serif; }
  .humanist { font-family: "Lato", sans-serif; }

  .never-stop {
    left: 29px; top: 30px;
    font-size: 25px; font-weight: 700; line-height: 35px; letter-spacing: 0.5px;
  }
  .bar {
    background: var(--ink);
    color: var(--sun);
  }
  .swoon {
    left: 22px; top: 114px; width: 499px; height: 60px;
    font-size: 30px; font-weight: 700; line-height: 60px; text-align: center;
    color: var(--sun);
  }
  .goals {
    left: 34px; top: 176px;
    font-size: 72px; font-weight: 700; line-height: 71px; letter-spacing: 1px;
  }
  .action-left {
    left: 31px; top: 398px;
    font-size: 26px; line-height: 31px;
  }
  .fail-stop {
    left: 541px; top: 29px; height: 440px; width: 38px;
    writing-mode: vertical-rl; transform: rotate(180deg);
    font-size: 32px; line-height: 38px; text-align: left;
  }
  .chase-caps {
    left: 598px; top: 26px;
    font-size: 33px; line-height: 38px; text-transform: uppercase;
  }
  .rule {
    height: 1px; background: var(--ink);
  }
  .rule-top { left: 601px; top: 107px; width: 373px; }
  .rule-mid { left: 601px; top: 299px; width: 373px; }
  .action-right {
    left: 598px; top: 114px;
    font-size: 21px; line-height: 27px; letter-spacing: 0.3px;
  }
  .sleep-less {
    left: 601px; top: 175px;
    font-size: 62px; font-weight: 700; line-height: 61px; letter-spacing: 1px;
  }
  .dream-it {
    left: 605px; top: 302px;
    font-size: 37px; line-height: 46px;
  }
  .energy {
    left: 593px; top: 354px; width: 385px; height: 33px;
    font-size: 15px; line-height: 33px; text-align: center; text-transform: uppercase;
    color: var(--sun);
  }
  .motivates-right {
    left: 602px; top: 396px;
    font-size: 25px; line-height: 32px;
  }
  .chase-vertical {
    left: 987px; top: 26px; height: 440px; width: 30px;
    writing-mode: vertical-rl;
    font-size: 24px; font-weight: 700; line-height: 30px;
  }
  .chase-big {
    left: 32px; top: 480px;
    font-size: 63px; font-weight: 700; line-height: 70px; letter-spacing: 0.5px;
  }
  .dream-awake {
    left: 420px; top: 485px; width: 405px;
    font-size: 26px; font-weight: 700; line-height: 34.5px;
    text-align: justify; text-align-last: left; letter-spacing: 0.5px;
  }
  .right-easy {
    left: 31px; top: 692px;
    font-size: 55px; line-height: 64px; white-space: nowrap;
  }
  .motivates-vertical {
    left: 858px; top: 480px; height: 270px; width: 46px;
    writing-mode: vertical-rl; transform: rotate(180deg);
    font-size: 18px; line-height: 23px;
  }
  .dream-more-tag {
    left: 923px; top: 490px; width: 87px; height: 258px;
    display: flex; align-items: center; justify-content: center;
  }
  .dream-more-tag span {
    writing-mode: vertical-rl; transform: rotate(180deg);
    font-size: 40px; font-weight: 700; color: var(--sun);
  }
</style>
</head>
<body>
<main class="canvas">
  <section class="card" aria-label="Inspirational card front">
    <p class="never-stop serif">Never stop dreaming --- most realities<br>were once created from dreams.</p>

    <p class="swoon bar sans">SWOON, SLUMBER, REPEAT</p>

    <h1 class="goals serif">Goals are just<br>dreams with<br>a deadline</h1>

    <p class="action-left sans">What's one action I can take today<br>to make my goal feel more achievable?</p>

    <p class="fail-stop sans">You only fail when you stop</p>

    <p class="chase-caps serif">Don't follow your<br>dream chase them!</p>
    <div class="rule rule-top"></div>

    <p class="action-right humanist">What's one action I can take today<br>to make my goal feel more achievable?</p>

    <h2 class="sleep-less serif">Sleep Less,<br>Dream More</h2>
    <div class="rule rule-mid"></div>

    <p class="dream-it serif">Dream it, wish it, do it</p>

    <p class="energy bar serif">Be the energy you want to attract</p>

    <p class="motivates-right sans">What motivates you to keep<br>going when things get tough?</p>

    <p class="chase-vertical serif">Don't follow your dream chase them!</p>

    <h2 class="chase-big serif">Don't follow<br>your &nbsp;dream<br>chase them!</h2>

    <p class="dream-awake serif">A dream is not something that happens while you sleep, its what keeps you awake and striving for something greater every day</p>

    <p class="right-easy sans">Do what is right, not what is easy</p>

    <p class="motivates-vertical sans">What motivates you to keep<br>going when things get tough?</p>

    <div class="dream-more-tag bar"><span class="serif">Dream More</span></div>
  </section>
</main>
</body>
</html>
```